Lidia Vanta Catering
Complete Stationery Design
Lidia Vanta Catering - Chef / Catering
Creative Brief
Bright & Fun-filled
Corazon Belmiro
Director, Sales & Marketing
2nd Floor, Quintero Bldg., Saldivar Avenue near corner Lupine Street, Navotas, Metro Manila, Philippines 1490
cbelmiro@lidiavanta-example.ph
www.lidiavanta-example.ph
Lidia Vanta is a high end catering company. Our design is modern Victorian. Color dark red, black and white but we are open to other color suggestion. We need the ff: - business cards - A4 and letter size paper with matching letter envelopes - Folder that fits A4 and letter size envelop - Fax Cover - CD sticker and cover - Sticker label - Address Sticker Label - Paper Bag Design - Styro lunch box design - Tissue Napkin Design - Name Plate - Identification Card Design
Victorian design with our Logo in the middle

```html
<!DOCTYPE html>
<html lang="en">
<head>
<meta charset="utf-8">
<title>Lidia Vanta Catering – Business Cards</title>
<link rel="stylesheet" href="https://fonts.googleapis.com/css2?family=Crimson+Text:ital,wght@0,400;0,600;1,400&family=Open+Sans:ital,wght@1,700&display=swap">
<style>
  :root {
    --bg: #ece9e4;
    --card: #ffffff;
    --red: #d3121a;
    --black: #1a1a1a;
    --grey: #555555;
    --rule: #c9c9c9;
  }
  * { box-sizing: border-box; margin: 0; padding: 0; }
  html, body { width: 1200px; height: 852px; overflow: hidden; background: var(--bg); }
  .stage { position: relative; width: 1200px; height: 852px; }
  .card {
    position: absolute; top: 271px; width: 540px; height: 310px;
    background: var(--card); border-radius: 14px; overflow: hidden;
    box-shadow: 0 6px 18px rgba(0,0,0,.18);
    font-family: "Crimson Text", Georgia, serif; color: var(--black);
  }
  .card--centered { left: 40px; }
  .card--stacked { left: 620px; }
  .swoosh { position: absolute; left: 0; bottom: 0; width: 540px; height: 310px; }
  .ornament {
    position: absolute; width: 110px; height: 42px; border-radius: 50% 50% 6px 6px;
    background: linear-gradient(180deg, #f2f2f2, #cfcfcf);
  }
  .brand { position: absolute; font-size: 27px; font-weight: 400; color: var(--black); white-space: nowrap; line-height: 1.1; }
  .person { position: absolute; white-space: nowrap; }
  .person__name { font-family: "Open Sans", Arial, sans-serif; font-style: italic; font-weight: 700; color: var(--red); font-size: 15px; }
  .person__title { font-family: "Open Sans", Arial, sans-serif; font-style: italic; font-weight: 700; color: var(--black); font-size: 11px; }
  .address { position: absolute; font-size: 13px; line-height: 15px; color: var(--grey); }
  .divider { position: absolute; width: 1px; background: var(--rule); }
  .contacts { position: absolute; list-style: none; font-size: 11px; line-height: 16px; color: var(--grey); }
  .contacts li { display: flex; align-items: center; gap: 7px; white-space: nowrap; }
  .contacts svg { width: 11px; height: 11px; flex: none; }
</style>
</head>
<body>
<div class="stage">

  <section class="card card--centered">
    <svg class="swoosh" viewBox="0 0 540 310" aria-hidden="true">
      <path d="M0 300 C150 262 330 236 540 222 L540 310 L0 310 Z" fill="var(--red)"/>
      <path d="M0 292 C160 250 340 224 540 214 L540 222 C330 236 150 262 0 300 Z" fill="var(--black)"/>
      <path d="M0 283 C170 240 350 216 540 208 L540 211 C350 220 170 244 0 288 Z" fill="var(--black)"/>
    </svg>
    <div class="ornament" role="img" aria-label="Victorian ornament above the name" style="left:215px;top:18px"></div>
    <div class="brand" style="left:0;width:540px;text-align:center;top:64px">Lidia Vanta Catering</div>
    <div class="person" style="left:70px;top:108px"><span class="person__name">Corazon Belmiro</span> <span class="person__title">/ Director, Sales &amp; Marketing</span></div>
    <p class="address" style="left:40px;top:134px;width:190px">2nd Floor, Quintero Bldg.,<br>Saldivar Avenue<br>Near corner Lupine Street<br>Navotas, Metro Manila<br>Philippines 1490</p>
    <div class="divider" style="left:240px;top:136px;height:68px"></div>
    <ul class="contacts" style="left:252px;top:136px">
      <li><svg viewBox="0 0 12 12"><path d="M2 1 L4.5 1 L5.5 3.5 L4 4.5 C4.8 6.2 5.8 7.2 7.5 8 L8.5 6.5 L11 7.5 L11 10 C6 10.5 1.5 6 2 1 Z" fill="var(--red)"/></svg>+632 555 0184</li>
      <li><svg viewBox="0 0 12 12"><rect x="3" y="0.5" width="6" height="11" rx="1.2" fill="var(--red)"/><rect x="4" y="2" width="4" height="6" fill="#fff"/></svg>+63917 555 0236</li>
      <li><svg viewBox="0 0 12 12"><circle cx="6" cy="6" r="5.5" fill="var(--red)"/><rect x="3" y="4" width="6" height="4" fill="#fff"/></svg>cbelmiro@lidiavanta-example.ph</li>
      <li><svg viewBox="0 0 12 12"><circle cx="6" cy="6" r="5.5" fill="var(--red)"/><circle cx="6" cy="6" r="2.5" fill="#fff"/></svg>www.lidiavanta-example.ph</li>
    </ul>
  </section>

  <section class="card card--stacked">
    <svg class="swoosh" viewBox="0 0 540 310" aria-hidden="true">
      <path d="M0 300 C150 262 330 236 540 222 L540 310 L0 310 Z" fill="var(--red)"/>
      <path d="M0 292 C160 250 340 224 540 214 L540 222 C330 236 150 262 0 300 Z" fill="var(--black)"/>
      <path d="M0 283 C170 240 350 216 540 208 L540 211 C350 220 170 244 0 288 Z" fill="var(--black)"/>
    </svg>
    <div class="person" style="left:205px;top:20px"><div class="person__name">Corazon Belmiro</div><div class="person__title">Director, Sales &amp; Marketing</div></div>
    <p class="address" style="left:205px;top:62px;width:200px">2nd Floor, Quintero Bldg.,<br>Saldivar Avenue<br>Near corner Lupine Street<br>Navotas, Metro Manila<br>Philippines 1490</p>
    <div class="ornament" role="img" aria-label="Victorian ornament above the name" style="left:60px;top:108px;width:100px;height:36px"></div>
    <div class="brand" style="left:10px;width:230px;text-align:center;top:148px;font-size:23px">Lidia Vanta Catering</div>
    <div class="divider" style="left:258px;top:142px;height:64px"></div>
    <ul class="contacts" style="left:268px;top:142px">
      <li><svg viewBox="0 0 12 12"><path d="M2 1 L4.5 1 L5.5 3.5 L4 4.5 C4.8 6.2 5.8 7.2 7.5 8 L8.5 6.5 L11 7.5 L11 10 C6 10.5 1.5 6 2 1 Z" fill="var(--red)"/></svg>+632 555 0184</li>
      <li><svg viewBox="0 0 12 12"><rect x="3" y="0.5" width="6" height="11" rx="1.2" fill="var(--red)"/><rect x="4" y="2" width="4" height="6" fill="#fff"/></svg>+63917 555 0236</li>
      <li><svg viewBox="0 0 12 12"><circle cx="6" cy="6" r="5.5" fill="var(--red)"/><rect x="3" y="4" width="6" height="4" fill="#fff"/></svg>cbelmiro@lidiavanta-example.ph</li>
      <li><svg viewBox="0 0 12 12"><circle cx="6" cy="6" r="5.5" fill="var(--red)"/><circle cx="6" cy="6" r="2.5" fill="#fff"/></svg>www.lidiavanta-example.ph</li>
    </ul>
  </section>

</div>
</body>
</html>
```